We require a banner design for a 53' x 10' trailer for a future development to be displayed on the side of the highway. The development name is 712 35 Commerce Park, logo is attached. This is an industrial future development. Please also include the RLW Group logo and MERO Development logos as well.

Industry/Entity Type

Real Estate / Construction / Developer / Industrial Future Development

Requirements
Must have
• Logos provided

```html
<!DOCTYPE html>
<html lang="en">
<head>
<meta charset="utf-8">
<title>712 35 Commerce Park – Trailer Banner</title>
<link href="https://fonts.googleapis.com/css2?family=Montserrat:wght@500;600;800&family=Oswald:wght@600&family=Great+Vibes&display=swap" rel="stylesheet">
<style>
  :root {
    --stage: #6b6b6b;
    --ink: #141414;
    --brown: #5a4a42;
    --red: #d8111f;
    --red-deep: #a80b14;
    --white: #ffffff;
    --panel-dark: #0c0c0c;
    --panel-mid: #2a2a2a;
    --paper: #ffffff;
    --paper-grey: #d9d9d9;
  }
  * { box-sizing: border-box; margin: 0; padding: 0; }
  html, body { width: 1200px; height: 581px; overflow: hidden; background: var(--stage); }
  .banner {
    position: absolute; left: 78px; top: 157px; width: 1046px; height: 267px;
    background: linear-gradient(100deg, var(--paper) 45%, #f1f1f1 70%, var(--paper-grey) 100%);
    overflow: hidden;
  }
  .banner__dark-panel {
    position: absolute; left: 0; top: 0; width: 206px; height: 100%;
    background: linear-gradient(135deg, var(--panel-mid) 0%, var(--panel-dark) 45%, #1c1c1c 70%, var(--panel-dark) 100%);
  }
  .coming-soon { position: absolute; left: 48px; top: 30px; width: 312px; height: 196px; }
  .coming-soon svg { position: absolute; inset: 0; }
  .coming-soon__top, .coming-soon__main {
    position: absolute; width: 100%; text-align: center; color: var(--white);
    text-shadow: 3px 3px 0 var(--red-deep);
  }
  .coming-soon__top {
    top: 36px; left: -6px; font-family: "Montserrat", sans-serif; font-weight: 800; font-size: 41px; letter-spacing: 0.5px;
    transform: rotate(-3deg);
  }
  .coming-soon__main {
    top: 76px; left: -4px; font-family: "Oswald", sans-serif; font-weight: 600; font-size: 92px; line-height: 1;
    transform: rotate(-2deg);
  }
  .park-name {
    position: absolute; left: 392px; top: 40px; width: 260px;
    font-family: "Montserrat", sans-serif; font-weight: 600; color: var(--ink);
  }
  .park-name__number { font-size: 84px; line-height: 76px; letter-spacing: -1px; }
  .park-name__row { display: flex; align-items: center; gap: 18px; }
  .park-name__square { width: 56px; height: 56px; background: var(--brown); }
  .park-name__label { font-size: 22px; letter-spacing: 2px; margin-top: 4px; }
  .tagline { position: absolute; left: 684px; top: 48px; font-family: "Montserrat", sans-serif; }
  .tagline__first { font-weight: 800; font-size: 33px; color: var(--ink); letter-spacing: 0.3px; }
  .tagline__second { display: flex; align-items: baseline; margin-top: -4px; }
  .tagline__script { font-family: "Great Vibes", cursive; font-size: 50px; color: var(--ink); }
  .tagline__strong { font-weight: 800; font-size: 55px; color: var(--brown); margin-left: -2px; }
  .powered-by {
    position: absolute; left: 686px; top: 151px; width: 220px; height: 28px;
    background: var(--red); border-radius: 3px; box-shadow: 2px 3px 0 #7a6a62;
    color: var(--white); font-family: "Montserrat", sans-serif; font-weight: 800;
    font-size: 19px; letter-spacing: 3.5px; text-align: center; line-height: 28px;
  }
  .partner { position: absolute; top: 200px; display: flex; align-items: center; gap: 8px;
    font-family: "Montserrat", sans-serif; font-weight: 600; color: var(--ink); }
  .partner--mero { left: 686px; }
  .partner--rlw { left: 862px; }
  .partner__square { width: 30px; height: 30px; background: var(--red); }
  .partner__circle { width: 26px; height: 26px; border-radius: 50%; background: var(--red); }
  .partner__name { font-size: 24px; letter-spacing: 1.5px; line-height: 1; }
  .partner__sub { display: block; font-size: 7px; letter-spacing: 1px; margin-top: 4px; }
</style>
</head>
<body>
  <section class="banner">
    <div class="banner__dark-panel" role="img" aria-label="Dark faceted geometric background"></div>

    <div class="coming-soon">
      <svg viewBox="0 0 312 196" width="312" height="196" aria-hidden="true">
        <path d="M14 42 Q14 28 28 27 L290 6 Q304 5 304 19 L304 180 Q304 192 292 191 L28 174 Q14 173 14 160 Z" fill="#5a4a42"/>
        <path d="M4 34 Q4 20 18 19 L284 0 Q298 0 298 14 L298 172 Q298 184 286 184 L18 166 Q4 165 4 152 Z" fill="var(--red)"/>
      </svg>
      <div class="coming-soon__top">COMING</div>
      <div class="coming-soon__main">SOON!</div>
    </div>

    <div class="park-name">
      <div class="park-name__number">712</div>
      <div class="park-name__row">
        <span class="park-name__square"></span>
        <span class="park-name__number">35</span>
      </div>
      <div class="park-name__label">COMMERCE PARK</div>
    </div>

    <div class="tagline">
      <div class="tagline__first">YOUR BUSINESS</div>
      <div class="tagline__second">
        <span class="tagline__script">Our</span>
        <span class="tagline__strong">FUTURE</span>
      </div>
    </div>

    <div class="powered-by">POWERED BY</div>

    <div class="partner partner--mero">
      <span class="partner__square"></span>
      <span class="partner__name">MERO<span class="partner__sub">DEVELOPMENT</span></span>
    </div>

    <div class="partner partner--rlw">
      <span class="partner__circle"></span>
      <span class="partner__name">RLW GROUP</span>
    </div>
  </section>
</body>
</html>
```